Elegant Business Card with Logo and Picture

Please create a business card that has the Logo colors add Gold and turquoise / use the attached logo - I would like a beautiful Business Card - Please make sure it's printed on both sides / Picture can go on one side Logo other
www.velmorshine.example
614-372-0586
Lyn Odessa Ferwick
lynodessaf@quillpost.example
Life Coach
Vantrell Certified Teacher / Life Coach / Interior Designer
Transformational Retreats

Target Market(s)

Women Men General

Industry/Entity Type

Life Coaching

Contact Information for Business Card

www.velmorshine.example
614-372-0586
Lyn Odessa Ferwick
Life Coach
Vantrell Certified Teacher / Yoga Teacher / Interior Designer

Font styles to use
Serif
Decorative

Colors
33a6d6
e34197
ffc214

Requirements
Must have
• Quality Paper and touch /
Nice to have
• Beautiful Touch and feel
Should not have
• needs to be elegant

```html
<!DOCTYPE html>
<html lang="en">
<head>
<meta charset="utf-8">
<title>Velmor Shine Coaching – Business Card</title>
<link rel="stylesheet" href="https://fonts.googleapis.com/css2?family=Libre+Baskerville:wght@700&family=Roboto:wght@400;700&family=Roboto+Condensed:wght@400&display=swap">
<style>
  :root {
    --backdrop: #d9d9d9;
    --card-white: #ffffff;
    --card-dark: #1c1c1e;
    --card-dark-edge: #2a2a2d;
    --pattern-tone: #34282f;
    --magenta: #ec168c;
    --ink: #111111;
    --muted: #555555;
    --photo-light: #efe4d2;
    --photo-mid: #dcc08f;
    --photo-warm: #c98a72;
  }
  html, body {
    margin: 0;
    width: 1200px;
    height: 1200px;
    overflow: hidden;
    background: var(--backdrop);
  }
  .canvas { position: relative; width: 1200px; height: 1200px; }
  .card {
    position: absolute;
    left: 262px;
    width: 685px;
    height: 392px;
    border-radius: 18px;
    overflow: hidden;
  }
  .card-front { top: 165px; background: var(--card-white); }
  .card-back {
    top: 653px;
    background: linear-gradient(180deg, var(--card-dark-edge), var(--card-dark));
  }
  .portrait {
    position: absolute;
    left: 0; top: 0;
    width: 357px; height: 392px;
    background: radial-gradient(ellipse at 45% 38%, var(--photo-light) 0%, var(--photo-mid) 50%, var(--photo-warm) 100%);
  }
  .brand-tab {
    position: absolute;
    left: 473px; top: 0;
    width: 100px; height: 58px;
    background: var(--magenta);
  }
  .brand-name {
    position: absolute;
    font-family: "Roboto", sans-serif;
    font-weight: 700;
    line-height: 1;
    margin: 0;
  }
  .brand-name-front {
    left: 453px; top: 74px;
    width: 140px;
    text-align: center;
    font-size: 44px;
    color: var(--ink);
  }
  .company {
    position: absolute;
    left: 396px; top: 150px;
    width: 272px;
    text-align: center;
  }
  .company-name {
    font-family: "Libre Baskerville", serif;
    font-weight: 700;
    font-size: 18px;
    letter-spacing: 3px;
    color: var(--ink);
    margin: 0;
  }
  .company-tagline {
    font-family: "Roboto", sans-serif;
    font-size: 9px;
    letter-spacing: 11px;
    color: var(--magenta);
    margin: 2px 0 0 8px;
  }
  .person {
    position: absolute;
    left: 396px; top: 207px;
  }
  .person-name {
    font-family: "Roboto", sans-serif;
    font-weight: 700;
    font-size: 23px;
    color: var(--magenta);
    margin: 0 0 6px;
  }
  .person-roles {
    font-family: "Roboto Condensed", sans-serif;
    font-size: 15.5px;
    line-height: 19.5px;
    color: var(--ink);
    margin: 0 0 10px;
  }
  .contact-list { list-style: none; margin: 0; padding: 0; }
  .contact-list li {
    display: flex;
    align-items: center;
    gap: 8px;
    font-family: "Roboto", sans-serif;
    font-size: 15.5px;
    line-height: 19.5px;
    color: var(--muted);
  }
  .contact-list svg { width: 13px; height: 13px; fill: var(--magenta); flex: none; }
  .back-pattern {
    position: absolute;
    inset: 0;
    background:
      radial-gradient(ellipse at 30% 35%, rgba(236, 22, 140, 0.07), transparent 60%),
      radial-gradient(ellipse at 75% 70%, rgba(236, 22, 140, 0.05), transparent 55%),
      linear-gradient(180deg, var(--pattern-tone), var(--card-dark));
  }
  .brand-name-back {
    left: 540px; top: 278px;
    width: 120px;
    text-align: center;
    font-size: 44px;
    color: #ffffff;
  }
  .edge-accent {
    position: absolute;
    left: 0; top: 324px;
    width: 3px; height: 36px;
    background: var(--magenta);
  }
</style>
</head>
<body>
<main class="canvas">
  <section class="card card-front">
    <div class="portrait" role="img" aria-label="Portrait photograph of the coach"></div>
    <div class="brand-tab"></div>
    <p class="brand-name brand-name-front">Lyn</p>
    <div class="company">
      <p class="company-name">VELMOR SHINE</p>
      <p class="company-tagline">COACHING</p>
    </div>
    <div class="person">
      <h1 class="person-name">Lyn Odessa Ferwick</h1>
      <p class="person-roles">Life Coach<br>Vantrell Certified Teacher /<br>Yoga Teacher / Interior Designer</p>
      <ul class="contact-list">
        <li><svg viewBox="0 0 24 24"><path d="M6.6 10.8a15 15 0 0 0 6.6 6.6l2.2-2.2c.3-.3.7-.4 1-.2 1.1.4 2.3.6 3.6.6.6 0 1 .4 1 1V20c0 .6-.4 1-1 1A17 17 0 0 1 3 4c0-.6.4-1 1-1h3.5c.6 0 1 .4 1 1 0 1.3.2 2.5.6 3.6.1.3 0 .7-.2 1z"/></svg>614-372-0586</li>
        <li><svg viewBox="0 0 24 24"><path d="M2 5h20v14H2z M2 5l10 8 10-8" stroke="#fff" stroke-width="1.5"/></svg>lynodessaf@quillpost.example</li>
        <li><svg viewBox="0 0 24 24"><circle cx="12" cy="12" r="10"/><path d="M7 8c2 1 3 3 2 5s1 3 3 4M14 4c0 3 3 3 5 5" stroke="#fff" stroke-width="1.5" fill="none"/></svg>www.velmorshine.example</li>
      </ul>
    </div>
  </section>

  <section class="card card-back">
    <div class="back-pattern" role="img" aria-label="Faint repeated brand pattern across the card back"></div>
    <div class="edge-accent"></div>
    <p class="brand-name brand-name-back">Lyn</p>
  </section>
</main>
</body>
</html>
```